Business Card Velostra - Accounting firm

Hi my friend.
I'm coming back to you to see if it would be possible for you to make a modern and minimalist business card design.
In shades of blue like the great logo you offered me.
The ideal is a modern and aesthetic business card.
The goal is to give a professional effect to the first exchanges.
Renewal and innovation in the accounting world !!
I thank you !!
Good evening to you

Target Market(s)

Young, dynamic and sensitive to marketing

Industry/Entity Type

Finance And Accounting

Contact Information for Business Card

Company logo and name. Last name, First name, Phone number, email address, company address, website.

Font styles to use
Sans Serif

Requirements
Must have
• The ideal is a modern and aesthetic business card.

Mentions to include: Company logo and name. Last name, First name, Phone number, email address, company address, website.
Nice to have
• The goal is to give a professional effect to the first exchanges.
Should not have
• Simplistic or childish design

```html
<!DOCTYPE html>
<html lang="en">
<head>
<meta charset="utf-8">
<title>Velostra – Business Card</title>
<link rel="stylesheet" href="https://fonts.googleapis.com/css2?family=Source+Sans+3:wght@400;600&display=swap">
<style>
  :root {
    --backdrop: #e4e5e7;
    --navy: #1f2a5c;
    --teal: #5bbdb0;
    --blue: #1271bf;
    --paper: #f4f4f6;
    --name-accent: #55aac4;
    --white: #ffffff;
  }
  * { margin: 0; padding: 0; box-sizing: border-box; }
  html, body { width: 1200px; height: 960px; overflow: hidden; }
  body {
    background: var(--backdrop);
    font-family: "Source Sans 3", "Helvetica Neue", Arial, sans-serif;
    position: relative;
  }
  .card {
    position: absolute;
    left: 303px;
    width: 595px;
    height: 341px;
    overflow: hidden;
  }
  .card--front {
    top: 117px;
    background: var(--navy);
    display: flex;
    align-items: center;
    justify-content: center;
    gap: 18px;
  }
  .brand-mark {
    width: 44px;
    height: 44px;
    background: var(--teal);
  }
  .brand-name {
    font-weight: 600;
    font-size: 74px;
    letter-spacing: 1px;
    color: var(--white);
    line-height: 1;
  }
  .card--back { top: 510px; background: var(--paper); }
  .card__shapes { position: absolute; inset: 0; }
  .holder {
    position: absolute;
    left: 46px;
    top: 68px;
    color: var(--white);
  }
  .holder__name {
    font-weight: 600;
    font-size: 19px;
    color: var(--name-accent);
  }
  .holder__role { font-size: 15px; margin-top: 1px; }
  .contact {
    position: absolute;
    left: 46px;
    top: 199px;
    color: var(--white);
    font-size: 15px;
    line-height: 20px;
  }
  .contact__address { margin-bottom: 7px; }
  .contact__line { display: flex; align-items: center; gap: 6px; }
  .contact__line svg { width: 14px; height: 14px; flex: none; }
  .lockup {
    position: absolute;
    left: 370px;
    right: 0;
    top: 78px;
    display: flex;
    flex-direction: column;
    align-items: center;
  }
  .lockup .brand-mark { width: 100px; height: 100px; margin-bottom: 24px; }
  .lockup .brand-name { color: var(--navy); font-size: 48px; }
  .lockup__tagline {
    margin-top: 2px;
    font-weight: 600;
    font-size: 10px;
    letter-spacing: 3px;
    color: var(--navy);
  }
</style>
</head>
<body>
  <section class="card card--front" aria-label="Business card front">
    <div class="brand-mark" aria-hidden="true"></div>
    <div class="brand-name">velostra</div>
  </section>

  <section class="card card--back" aria-label="Business card back">
    <svg class="card__shapes" viewBox="0 0 595 341" aria-hidden="true">
      <defs>
        <linearGradient id="contactBand" x1="0" y1="0" x2="1" y2="0.8">
          <stop offset="0" stop-color="var(--teal)"/>
          <stop offset="0.75" stop-color="var(--blue)"/>
        </linearGradient>
      </defs>
      <polygon points="0,0 370,0 280,167 0,167" fill="var(--navy)"/>
      <polygon points="0,174 280,174 370,341 0,341" fill="url(#contactBand)"/>
    </svg>

    <div class="holder">
      <div class="holder__name">Daniel Mercer</div>
      <div class="holder__role">President</div>
    </div>

    <div class="contact">
      <div class="contact__address">48 Harbor Lane, Suite 310<br>Coral Bay, Florida, 33450</div>
      <div class="contact__line">
        <svg viewBox="0 0 16 16"><path fill="var(--navy)" d="M3.5 1.5l2.5 0 1 3.5-1.6 1.2a8 8 0 0 0 4.4 4.4L11 9l3.5 1v2.5c0 1-1 2-2 2A11 11 0 0 1 1.5 3.5c0-1 1-2 2-2z"/></svg>
        <span>(555) 274-1938</span>
      </div>
      <div class="contact__line">
        <svg viewBox="0 0 16 16"><rect x="1.5" y="3.5" width="13" height="9" fill="none" stroke="var(--navy)" stroke-width="1.6"/><path d="M1.5 3.5l6.5 5 6.5-5" fill="none" stroke="var(--navy)" stroke-width="1.6"/></svg>
        <span>daniel@velostraweb.com</span>
      </div>
      <div class="contact__line">
        <svg viewBox="0 0 16 16"><g fill="none" stroke="var(--navy)" stroke-width="1.3"><circle cx="8" cy="8" r="6.3"/><ellipse cx="8" cy="8" rx="2.7" ry="6.3"/><path d="M1.7 8h12.6M2.7 4.8h10.6M2.7 11.2h10.6"/></g></svg>
        <span>www.velostraweb.com</span>
      </div>
    </div>

    <div class="lockup">
      <div class="brand-mark" aria-hidden="true"></div>
      <div class="brand-name">velostra</div>
      <div class="lockup__tagline">EXPERT-COMPTABLE</div>
    </div>
  </section>
</body>
</html>
```